Anti-Pelkin website needing sticker designs

We are a website promoting the number of days until the 2020 Presidential election (done), give individuals a place to voice their opinions about the current administration (in progress), and purchase merchandise such as bumper stickers, beer coozies, t-shirts, etc. (in progress). Visit NotPelkin2020.com to see more. We would like to see standard "NOTPELKIN2020.com" bumper stickers, as well as images for stickers portraying the him in a caricature like manner (think Salt Roads Beyond Marrow Creek movie cover), strung out, and other creative ways to express our discontent with the current administration. Most would need some way to incorporate "NotPelkin2020.com".
Industry/Entity Type
Political
Colors
Designer to choose colors to be used in the design.
Requirements
Nice to have
- We would like to see standard "NOT PELKIN 2020.com" bumper stickers, as well as images for stickers portraying the him in a caricature like manner (think Salt Roads Beyond Marrow Creek movie cover), strung out, and other creative ways to express our discontent with the current administration. Most would need some way to incorporate "NotPelkin2020.com".
Should not have
- Profanity, Threats, or anything perceived as such

```html
<!DOCTYPE html>
<html lang="en">
<head>
<meta charset="utf-8">
<title>Not Pelkin 2020 Bumper Sticker</title>
<link rel="stylesheet" href="https://fonts.googleapis.com/css2?family=Arimo:wght@700&display=swap">
<style>
  :root {
    --backdrop: #e2a0a0;
    --sticker-blue: #1f4a92;
    --sticker-blue-light: #2d66b0;
    --sticker-blue-dark: #17397a;
    --frame-white: #ffffff;
    --ban-red: #d10f14;
    --portrait-warm: #e89a5c;
    --portrait-hair: #e8c23a;
    --portrait-deep: #b9561e;
  }
  html, body {
    margin: 0;
    padding: 0;
    width: 1200px;
    height: 1200px;
    overflow: hidden;
    background: var(--backdrop);
  }
  .canvas {
    width: 1200px;
    height: 1200px;
    display: flex;
    align-items: center;
    justify-content: center;
  }
  .bumper-sticker {
    width: 1120px;
    height: 292px;
    display: block;
    filter: drop-shadow(0 6px 10px rgba(80, 20, 20, 0.35));
  }
  .sticker-text {
    font-family: "Arimo", Arial, sans-serif;
    font-weight: 700;
    fill: var(--frame-white);
  }
</style>
</head>
<body>
<main class="canvas">
  <svg class="bumper-sticker" viewBox="0 0 1400 365" xmlns="http://www.w3.org/2000/svg" aria-label="Not Pelkin 2020 bumper sticker">
    <defs>
      <linearGradient id="sticker-field" x1="0" y1="0" x2="1" y2="1">
        <stop offset="0" stop-color="var(--sticker-blue-dark)"/>
        <stop offset="0.45" stop-color="var(--sticker-blue-light)"/>
        <stop offset="1" stop-color="var(--sticker-blue)"/>
      </linearGradient>
      <radialGradient id="portrait-tone" cx="0.45" cy="0.45" r="0.6">
        <stop offset="0" stop-color="var(--portrait-warm)"/>
        <stop offset="0.35" stop-color="var(--portrait-hair)" stop-opacity="0.9"/>
        <stop offset="0.75" stop-color="var(--portrait-deep)"/>
        <stop offset="1" stop-color="var(--sticker-blue)" stop-opacity="0"/>
      </radialGradient>
    </defs>

    <rect class="sticker-field" x="0" y="0" width="1400" height="365" fill="url(#sticker-field)" role="img" aria-label="Swirling blue abstract background"/>

    <rect class="sticker-frame" x="39" y="30" width="1330" height="307" rx="12" fill="none" stroke="var(--frame-white)" stroke-width="4"/>

    <circle class="caricature-area" cx="294" cy="183" r="150" fill="url(#portrait-tone)" role="img" aria-label="Distorted caricature portrait of Pelkin"/>

    <g class="ban-sign" fill="none" stroke="var(--ban-red)" stroke-width="28">
      <circle cx="294" cy="183" r="153"/>
      <line x1="402" y1="75" x2="186" y2="291"/>
    </g>

    <text class="sticker-text headline-not" x="500" y="200" font-size="200">NOT</text>
    <text class="sticker-text headline-name" x="515" y="312" font-size="134" textLength="745" lengthAdjust="spacingAndGlyphs">PELKIN2020</text>
  </svg>
</main>
</body>
</html>
```